PowerPoint design MedoraVix

We need a PowerPoint set-up based upon our existing logo (see joint file)
Our company is operating in the health care and life science sector. We are mainly focussing on international business

Target Market(s)

International

Industry/Entity Type

health care and life sciences

Requirements
Must have
• Logos as added

```html
<!DOCTYPE html>
<html lang="en">
<head>
<meta charset="utf-8">
<title>MedoraVix Presentation Slides</title>
<link href="https://fonts.googleapis.com/css2?family=Open+Sans:wght@400;600;700&family=Roboto:wght@500;700&display=swap" rel="stylesheet">
<style>
:root{
  --stage:#dcdcde;
  --navy:#0b4a8b;
  --green:#55bf0c;
  --orange:#f49a0a;
  --purple:#6f4ea8;
  --slate:#37454b;
  --ink:#3a3a3a;
  --muted:#8a8a8a;
  --line:#cfcfcf;
  --white:#ffffff;
}
*{margin:0;padding:0;box-sizing:border-box}
html,body{width:1200px;height:696px;overflow:hidden;background:var(--stage)}
body{position:relative;font-family:"Open Sans",Arial,sans-serif;color:var(--ink)}
.slide{position:absolute;background:var(--white);overflow:hidden;box-shadow:0 1px 4px rgba(0,0,0,.25)}
.abs{position:absolute}
.title{font-family:"Roboto",Arial,sans-serif;font-weight:700;letter-spacing:-1px;color:var(--ink);line-height:1}
.subtitle{font-size:6px;color:var(--green)}
.brand{display:flex;align-items:center;gap:3px}
.brand-dot{width:14px;height:14px;border-radius:50%;background:var(--navy)}
.brand-name{font-size:10px;font-weight:700;color:var(--navy)}
.footer{position:absolute;right:9px;bottom:6px;height:8px;display:flex}
.footer-url{background:var(--slate);color:#fff;font-size:3.5px;padding:0 6px;line-height:8px}
.footer-num{background:var(--green);color:#fff;font-size:3.5px;width:11px;text-align:center;line-height:8px}
.tiny{font-size:4px;line-height:5.6px;color:var(--muted)}

/* hero price slide */
.hero{left:19px;top:18px;width:769px;height:432px}
.hero-photo{position:absolute;inset:0;background:radial-gradient(ellipse at 70% 55%,#8a5a3a 0%,#5a4a40 35%,#3e3a37 70%,#2c2a28 100%)}
.hero .title{color:#fff;font-size:34px;left:33px;top:32px}
.hero .hero-sub{color:#fff;font-size:12px;left:33px;top:66px}
.pack{position:absolute;color:#fff;padding:16px 0 0 28px}
.pack-basic{left:27px;top:131px;width:175px;height:219px;background:var(--navy)}
.pack-adv{left:202px;top:123px;width:182px;height:233px;background:var(--green);border-radius:4px}
.pack-name{font-size:14px}
.pack-price{font-size:25px;font-weight:700;line-height:1.1}
.pack-rule{height:2px;background:#fff;margin:10px 0 10px -12px;width:150px}
.pack-list{list-style:none;font-size:7.5px}
.pack-list li{height:24.5px}
.pack-list span{display:inline-block;width:15px}
.hero-page{left:735px;top:404px;color:#fff;font-size:7px}

/* plan grid slide */
.plans{left:804px;top:18px;width:379px;height:213px}
.plans .title{left:17px;top:15px;font-size:19px}
.plans .subtitle{left:17px;top:35px}
.plan{position:absolute;top:62px;width:76px;height:116px;border:1px dashed #9a9a9a;text-align:center}
.plan-name{font-size:7px;font-weight:600;margin-top:6px;color:#444}
.plan-price{margin:4px 3px 0;height:17px;color:#fff;font-size:9px;line-height:17px}
.plan-price small{font-size:4px}
.plan-item{font-size:3.6px;color:#777;height:17px;line-height:17px;margin:0 8px;border-bottom:1px solid #bbb}
.plan-item:last-child{border:none}

/* number list slide */
.numbers{left:804px;top:240px;width:379px;height:213px}
.numbers .kicker{left:36px;top:58px;font-size:7px;letter-spacing:2.6px}
.numbers .heading{left:36px;top:68px;font-size:18.5px;line-height:20.5px}
.num-item{position:absolute;left:186px;width:150px}
.num-box{position:absolute;left:0;top:0;width:23px;height:23px;color:#fff;font-weight:700;font-size:14px;text-align:center;line-height:23px}
.num-title{position:absolute;left:30px;top:0;font-size:6.5px;font-weight:700}
.num-text{position:absolute;left:30px;top:9px;width:110px}

/* services slide */
.services{left:18px;top:464px;width:378px;height:212px}
.services-band{position:absolute;left:0;top:0;width:100%;height:112px;background:var(--slate)}
.services .title{left:16px;top:15px;font-size:18px;color:#fff}
.services .subtitle{left:16px;top:34px}
.svc{position:absolute;top:74px;width:66px;height:63px;color:#fff;text-align:center}
.svc svg{margin-top:10px}
.svc-num{font-size:9px;font-weight:700;margin-top:4px;line-height:1}
.svc-label{font-size:4px}
.svc-text{position:absolute;top:146px;width:64px;text-align:justify}

/* iconic list slide */
.iconic{left:408px;top:464px;width:379px;height:212px}
.iconic .title{left:16px;top:14px;font-size:18px}
.iconic .subtitle{left:16px;top:34px}
.iconic-head{left:0;width:100%;top:51px;text-align:center;font-size:9px}
.iconic-intro{left:52px;width:275px;top:65px;text-align:center}
.feat{position:absolute;width:110px}
.feat svg{position:absolute;left:0;top:0}
.feat-title{position:absolute;left:24px;top:0;font-size:6px;font-weight:600}
.feat-text{position:absolute;left:24px;top:8px;width:78px}

/* process slide */
.process{left:803px;top:464px;width:379px;height:212px}
.process .title{left:16px;top:14px;font-size:18px}
.process .proc-sub{left:16px;top:35px;font-size:5.5px;color:#555}
.step-label{position:absolute;top:65px;width:80px;text-align:center;font-size:6.5px;font-weight:600}
.step-text{position:absolute;top:146px;width:76px;text-align:justify}
.brand-corner{position:absolute;right:16px;top:18px}
</style>
</head>
<body>

<!-- Hero pricing -->
<section class="slide hero">
  <div class="hero-photo" role="img" aria-label="Photo of a clay pot with cinnamon sticks and star anise on a wooden table"></div>
  <h1 class="title abs">Our Prices</h1>
  <p class="hero-sub abs">Insert Your Creative Idea</p>
  <div class="pack pack-basic">
    <div class="pack-name">Basic Pack</div>
    <div class="pack-price">$290</div>
    <div class="pack-rule"></div>
    <ol class="pack-list">
      <li><span>1.</span>Lorem Ipsum</li>
      <li><span>2.</span>Simply dummy</li>
      <li><span>3.</span>Text of the printing</li>
      <li><span>4.</span>Typesetting industry</li>
      <li><span>5.</span>Lorem Ipsum has</li>
    </ol>
  </div>
  <div class="pack pack-adv">
    <div class="pack-name">Adv. Pack</div>
    <div class="pack-price">$590</div>
    <div class="pack-rule"></div>
    <ol class="pack-list">
      <li><span>1.</span>Lorem Ipsum</li>
      <li><span>2.</span>Simply dummy</li>
      <li><span>3.</span>Text of the printing</li>
      <li><span>4.</span>Typesetting industry</li>
      <li><span>5.</span>Lorem Ipsum has</li>
    </ol>
  </div>
  <div class="hero-page abs">25</div>
</section>

<!-- Plan grid -->
<section class="slide plans">
  <h2 class="title abs">Our Prices</h2>
  <p class="subtitle abs">Insert Your Creative Idea</p>
  <div class="brand brand-corner"><span class="brand-dot"></span><span class="brand-name">MedoraVix</span></div>
  <div class="plan" style="left:32px"><div class="plan-name">STARTER</div><div class="plan-price" style="background:var(--navy)">$10 <small>/Month</small></div><div class="plan-item">5 USERS</div><div class="plan-item">10 PROJECTS</div><div class="plan-item">10 GB SPACE MEMORY</div><div class="plan-item">5 EMAIL ACCOUNT</div></div>
  <div class="plan" style="left:111px"><div class="plan-name">BASIC</div><div class="plan-price" style="background:var(--green)">$20 <small>/Month</small></div><div class="plan-item">5 USERS</div><div class="plan-item">10 PROJECTS</div><div class="plan-item">10 GB SPACE MEMORY</div><div class="plan-item">5 EMAIL ACCOUNT</div></div>
  <div class="plan" style="left:191px"><div class="plan-name">PROFESIONAL</div><div class="plan-price" style="background:var(--orange)">$30 <small>/Month</small></div><div class="plan-item">5 USERS</div><div class="plan-item">10 PROJECTS</div><div class="plan-item">10 GB SPACE MEMORY</div><div class="plan-item">5 EMAIL ACCOUNT</div></div>
  <div class="plan" style="left:271px"><div class="plan-name">ULTIMATE</div><div class="plan-price" style="background:var(--purple)">$40 <small>/Month</small></div><div class="plan-item">5 USERS</div><div class="plan-item">10 PROJECTS</div><div class="plan-item">10 GB SPACE MEMORY</div><div class="plan-item">5 EMAIL ACCOUNT</div></div>
  <div class="footer"><span class="footer-url">www.medoravix-care.com</span><span class="footer-num">24</span></div>
</section>

<!-- Number list -->
<section class="slide numbers">
  <div class="brand abs" style="left:32px;top:28px"><span class="brand-dot"></span><span class="brand-name">MedoraVix</span></div>
  <p class="kicker abs">NUMBER LIST</p>
  <h2 class="title heading abs">Insert Your<br>Creative<br>Idea</h2>
  <p class="tiny abs" style="left:36px;top:134px;width:110px">Clear care ideas help your audience trust your work and remember every key point.</p>
  <div class="num-item" style="top:50px"><div class="num-box" style="background:var(--navy)">01</div><div class="num-title">TARGET</div><p class="num-text tiny">Clear care ideas help your audience trust your work and remember every key point.</p></div>
  <div class="num-item" style="top:93px"><div class="num-box" style="background:var(--green)">02</div><div class="num-title">TARGET</div><p class="num-text tiny">Clear care ideas help your audience trust your work and remember every key point.</p></div>
  <div class="num-item" style="top:136px"><div class="num-box" style="background:var(--orange)">03</div><div class="num-title">TARGET</div><p class="num-text tiny">Clear care ideas help your audience trust your work and remember every key point.</p></div>
  <div class="footer"><span class="footer-url">www.medoravix-care.com</span><span class="footer-num">20</span></div>
</section>

<!-- Services -->
<section class="slide services">
  <div class="services-band"></div>
  <h2 class="title abs">Our Services</h2>
  <p class="subtitle abs">Insert Your Creative Idea</p>
  <div class="svc" style="left:30px;background:var(--navy)"><svg width="18" height="18" viewBox="0 0 18 18" fill="none" stroke="#fff" stroke-width="1.2"><circle cx="9" cy="9" r="8"/><circle cx="9" cy="9" r="5"/><circle cx="9" cy="9" r="2"/></svg><div class="svc-num">30.000+</div><div class="svc-label">SERVICES</div></div>
  <div class="svc" style="left:113px;background:var(--green)"><svg width="18" height="18" viewBox="0 0 18 18" fill="none" stroke="#fff" stroke-width="1.2"><path d="M3 8h10v5a3 3 0 0 1-3 3H6a3 3 0 0 1-3-3z"/><path d="M13 9h2a2 2 0 0 1 0 4h-2"/><path d="M6 2v4M8.5 2v4M11 2v4"/></svg><div class="svc-num">3.000+</div><div class="svc-label">SERVICES</div></div>
  <div class="svc" style="left:197px;background:var(--orange)"><svg width="18" height="18" viewBox="0 0 18 18" fill="none" stroke="#fff" stroke-width="1.2"><rect x="2" y="3" width="14" height="10"/><path d="M5 6h3v4H5zM10 7h4M10 9h4M9 13v3"/></svg><div class="svc-num">3.000+</div><div class="svc-label">SERVICES</div></div>
  <div class="svc" style="left:281px;background:var(--purple)"><svg width="18" height="18" viewBox="0 0 18 18" fill="none" stroke="#fff" stroke-width="1.2"><path d="M7 2h4M7.5 2v5L3 15h12L10.5 7V2"/><circle cx="8" cy="12" r=".8"/><circle cx="10.5" cy="11" r=".8"/></svg><div class="svc-num">30+</div><div class="svc-label">SERVICES</div></div>
  <p class="svc-text tiny" style="left:32px">Clear care ideas help your audience trust your work and remember every key point.</p>
  <p class="svc-text tiny" style="left:115px">Clear care ideas help your audience trust your work and remember every key point.</p>
  <p class="svc-text tiny" style="left:199px">Clear care ideas help your audience trust your work and remember every key point.</p>
  <p class="svc-text tiny" style="left:283px">Clear care ideas help your audience trust your work and remember every key point.</p>
  <div class="footer"><span class="footer-url">www.medoravix-care.com</span><span class="footer-num">23</span></div>
</section>

<!-- Iconic list -->
<section class="slide iconic">
  <h2 class="title abs">Iconic List</h2>
  <p class="subtitle abs">Insert Your Creative Idea</p>
  <div class="brand brand-corner"><span class="brand-dot"></span><span class="brand-name">MedoraVix</span></div>
  <p class="iconic-head abs">We Are <b>MedoraVix</b></p>
  <p class="iconic-intro tiny abs" style="color:#555">We bring life science and health care teams together across borders with simple tools, shared data and care that puts every patient first.</p>

  <div class="feat" style="left:17px;top:92px"><svg width="18" height="18" viewBox="0 0 18 18" fill="none" stroke-width="1.6"><circle cx="9" cy="9" r="6" stroke="var(--slate)"/><circle cx="9" cy="9" r="2.5" stroke="var(--green)"/></svg><div class="feat-title">TARGET</div><p class="feat-text tiny">Clear care ideas help your audience trust your work and remember every key point.</p></div>
  <div class="feat" style="left:139px;top:92px"><svg width="18" height="18" viewBox="0 0 18 18" fill="none" stroke-width="1.6"><path d="M3 16l4-6 4 6M7 10V5" stroke="var(--slate)"/><path d="M11 4l4 4-4 4" stroke="var(--green)"/></svg><div class="feat-title">STRATEGY</div><p class="feat-text tiny">Clear care ideas help your audience trust your work and remember every key point.</p></div>
  <div class="feat" style="left:261px;top:92px"><svg width="18" height="18" viewBox="0 0 18 18" fill="none" stroke-width="1.6"><rect x="5" y="4" width="8" height="12" stroke="var(--slate)"/><rect x="6.5" y="10" width="5" height="4.5" fill="var(--green)" stroke="none"/></svg><div class="feat-title">RESULT</div><p class="feat-text tiny">Clear care ideas help your audience trust your work and remember every key point.</p></div>
  <div class="feat" style="left:17px;top:147px"><svg width="18" height="18" viewBox="0 0 18 18" fill="none" stroke-width="1.6"><path d="M9 16S2 11 2 6a3.5 3.5 0 0 1 7-1 3.5 3.5 0 0 1 7 1c0 5-7 10-7 10z" stroke="var(--slate)"/><path d="M3 9h3l1.5-2 2 4 1.5-2h4" stroke="var(--green)"/></svg><div class="feat-title">CAMPAIGN</div><p class="feat-text tiny">Clear care ideas help your audience trust your work and remember every key point.</p></div>
  <div class="feat" style="left:139px;top:147px"><svg width="18" height="18" viewBox="0 0 18 18" fill="none" stroke-width="1.8"><path d="M9 2c-3 3-3 5 0 8l-5 6" stroke="var(--slate)"/><path d="M9 10l5 6" stroke="var(--green)"/></svg><div class="feat-title">CHARITY</div><p class="feat-text tiny">Clear care ideas help your audience trust your work and remember every key point.</p></div>
  <div class="feat" style="left:261px;top:147px"><svg width="18" height="18" viewBox="0 0 18 18" fill="none" stroke-width="1.8"><path d="M12 3l3 3" stroke="var(--slate)"/><path d="M13 5l-9 9-1 2" stroke="var(--green)"/></svg><div class="feat-title">OPTIMIZE</div><p class="feat-text tiny">Clear care ideas help your audience trust your work and remember every key point.</p></div>
  <div class="footer"><span class="footer-url">www.medoravix-care.com</span><span class="footer-num">19</span></div>
</section>

<!-- Process -->
<section class="slide process">
  <h2 class="title abs">Our Process</h2>
  <p class="proc-sub abs">Insert Your Creative Idea</p>
  <div class="brand brand-corner"><span class="brand-dot"></span><span class="brand-name">MedoraVix</span></div>
  <div class="step-label" style="left:43px">Creative Idea</div>
  <div class="step-label" style="left:150px">Creative Idea</div>
  <div class="step-label" style="left:257px">Creative Idea</div>
  <svg class="abs" style="left:0;top:80px" width="379" height="54" viewBox="0 0 379 54">
    <g stroke="#555" stroke-width="1"><line x1="43" y1="27" x2="123" y2="27"/><line x1="150" y1="27" x2="230" y2="27"/><line x1="254" y1="27" x2="336" y2="27"/></g>
    <g fill="#555"><circle cx="43" cy="27" r="1.5"/><circle cx="123" cy="27" r="1.5"/><circle cx="150" cy="27" r="1.5"/><circle cx="230" cy="27" r="1.5"/><circle cx="254" cy="27" r="1.5"/><circle cx="336" cy="27" r="1.5"/></g>
    <circle cx="83" cy="27" r="25" fill="var(--navy)"/>
    <circle cx="190" cy="27" r="25" fill="var(--green)"/>
    <circle cx="295" cy="27" r="25" fill="var(--orange)"/>
    <path d="M83 16v12a4 4 0 0 1-8 0M83 16a3 3 0 1 0 0 .1" fill="none" stroke="#fff" stroke-width="1.5"/>
    <g fill="#fff"><circle cx="190" cy="27" r="3"/><circle cx="190" cy="18" r="2"/><circle cx="198" cy="31" r="2"/><circle cx="182" cy="31" r="2"/></g>
    <g stroke="#fff" stroke-width="1.3"><line x1="190" y1="27" x2="190" y2="18"/><line x1="190" y1="27" x2="198" y2="31"/><line x1="190" y1="27" x2="182" y2="31"/></g>
    <ellipse cx="295" cy="26" rx="9" ry="6.5" fill="#fff"/>
  </svg>
  <p class="step-text tiny" style="left:45px">Clear care ideas help your audience trust your work and remember every key point.</p>
  <p class="step-text tiny" style="left:152px">Clear care ideas help your audience trust your work and remember every key point.</p>
  <p class="step-text tiny" style="left:257px">Clear care ideas help your audience trust your work and remember every key point.</p>
  <div class="footer"><span class="footer-url">www.medoravix-care.com</span><span class="footer-num">27</span></div>
</section>

</body>
</html>
```